Namecard Designs+Logo for a High End Automobile Company

We need a new business card for our company called Velta Motorhof.

www.veltamotorhof.example.sg
Our new website will be up in 2.5 months time.

We sell used and brand new continental cars like Korvane, QTL, Dravell, Solbrini and etc. Currently we are operating from 2 offices in Singapore and United Kingdom.

We want a design which is serious. We are open to colours but try to keep it at a maximum of 3 colours.

We prefer something simple and minimal. We are open to 2 sides printing or even 2 sided namecards. Both UK and Singapore company offices address must be in; either side by side, front and back, or even 2 sided cards.

The logo can be a text logo, emblem, abstract, pictorial or combination.

We are printing with Pribo.com so please kindly follow the printing guideline.

http://uk.pribo.example/help/faq/templates-and-guidelines.html

Rich and Car Enthusiasts

Printing

Must have
• Our 2 offices; UK and Singapore.

Our slogan which is " The Automobile Specialist"
Should not have
• Not more than 3 colours

```html
<!DOCTYPE html>
<html lang="en">
<head>
<meta charset="utf-8">
<title>Velta Motorhof — Business Card, Front and Back</title>
<link rel="stylesheet" href="https://fonts.googleapis.com/css2?family=Ubuntu:wght@400;500;700&display=swap">
<style>
  :root {
    --stage: #2a2a2a;
    --stage-stripe: #222222;
    --sheet: #c9c9c9;
    --bleed-area: #ffffff;
    --guide: #1a1a1a;
    --card-top: #474747;
    --card-bottom: #000000;
    --trim-green: #8cc63e;
    --brand-cyan: #12aee8;
    --office-teal: #26a7b5;
    --title-blue: #1477c2;
    --body-text: #f2f2f2;
    --label-white: #ffffff;
  }
  * { box-sizing: border-box; margin: 0; padding: 0; }
  html, body { width: 1200px; height: 900px; overflow: hidden; }
  body {
    position: relative;
    font-family: "Ubuntu", Arial, sans-serif;
    background: repeating-linear-gradient(135deg, var(--stage) 0 6px, var(--stage-stripe) 6px 9px);
  }
  .side-label {
    position: absolute;
    color: var(--label-white);
    font-size: 40px;
    font-weight: 400;
    line-height: 1;
  }
  .side-label--front { left: 834px; top: 26px; }
  .side-label--back { left: 107px; top: 340px; }

  .print-sheet {
    position: absolute;
    background: var(--sheet);
    box-shadow: 0 2px 6px rgba(0,0,0,.5);
  }
  .print-sheet--front { left: 340px; top: 62px; width: 812px; height: 545px; }
  .print-sheet--back { left: 23px; top: 377px; width: 665px; height: 447px; }

  .bleed-zone {
    position: absolute;
    inset: 17px;
    background: var(--bleed-area);
    border: 2px dashed var(--guide);
  }
  .guide-tag {
    position: absolute;
    font-size: 9px;
    font-weight: 700;
    color: var(--guide);
    letter-spacing: .3px;
  }
  .guide-tag--bleed { right: 4px; top: 3px; }
  .guide-tag--trim { right: 20px; top: 21px; }
  .scissors { position: absolute; top: 9px; width: 22px; height: 14px; }
  .print-sheet--front .scissors { right: 100px; }
  .print-sheet--back .scissors { right: 98px; }

  .edge-arrow { position: absolute; width: 10px; height: 10px; }
  .edge-arrow--top { left: 50%; top: 3px; margin-left: -5px; }
  .edge-arrow--bottom { left: 50%; bottom: 3px; margin-left: -5px; }
  .edge-arrow--left { top: 50%; left: 3px; margin-top: -5px; }
  .edge-arrow--right { top: 50%; right: 3px; margin-top: -5px; }

  .card-face {
    position: absolute;
    overflow: hidden;
    background: linear-gradient(180deg, var(--card-top) 0%, #1a1a1a 55%, var(--card-bottom) 100%);
    border: 2px solid var(--trim-green);
  }
  .print-sheet--front .card-face { left: 35px; top: 37px; right: 39px; bottom: 39px; }
  .print-sheet--back .card-face { left: 29px; top: 30px; right: 30px; bottom: 30px; }

  /* Front */
  .brand-block { position: absolute; left: 140px; top: 52px; }
  .brand-rule { position: absolute; left: 0; top: 0; width: 2px; height: 108px; background: #5a5a5a; }
  .brand-name {
    position: absolute; left: 18px; top: 10px;
    color: var(--brand-cyan);
    font-weight: 700;
    font-size: 32px;
    line-height: 30px;
    letter-spacing: 3px;
    white-space: nowrap;
  }
  .brand-slogan {
    position: absolute; left: 18px; top: 75px;
    color: var(--brand-cyan);
    font-size: 20px;
    white-space: nowrap;
    letter-spacing: .3px;
  }
  .office { position: absolute; left: 377px; }
  .office--uk { top: 322px; }
  .office--sg { top: 380px; }
  .office-name { color: var(--office-teal); font-size: 17px; font-weight: 400; line-height: 20px; }
  .office-address {
    margin-left: 56px;
    color: var(--body-text);
    font-size: 14px;
    line-height: 16px;
    font-style: normal;
  }

  /* Back */
  .corner-swoosh { position: absolute; right: 0; top: 0; width: 240px; height: 72px; }
  .holder { position: absolute; left: 0; right: 0; top: 143px; text-align: center; }
  .holder-name { color: var(--brand-cyan); font-size: 23px; font-weight: 400; line-height: 28px; }
  .holder-rule { width: 311px; height: 2px; margin: 2px auto 0; background: #e6e6e6; }
  .holder-title {
    display: inline-block;
    width: 119px;
    margin-left: -5px;
    padding: 2px 0 3px;
    background: var(--title-blue);
    border-radius: 0 0 5px 5px;
    color: var(--label-white);
    font-size: 14px;
  }
  .info-block { position: absolute; top: 286px; }
  .info-block--address { left: 24px; width: 250px; }
  .info-block--contact { left: 415px; }
  .info-label { color: var(--brand-cyan); font-size: 15px; line-height: 20px; margin-bottom: 3px; }
  .info-text { color: var(--body-text); font-size: 12.5px; line-height: 16px; font-style: normal; }
  .info-text--contact { line-height: 21px; }
</style>
</head>
<body>
  <div class="side-label side-label--front">Front</div>

  <section class="print-sheet print-sheet--front" aria-label="Card front">
    <div class="bleed-zone"></div>
    <span class="guide-tag guide-tag--bleed">BLEED</span>
    <span class="guide-tag guide-tag--trim">TRIM</span>
    <svg class="scissors" viewBox="0 0 22 14" aria-hidden="true">
      <circle cx="4" cy="4" r="2.6" fill="none" stroke="#111" stroke-width="1.4"/>
      <circle cx="4" cy="10" r="2.6" fill="none" stroke="#111" stroke-width="1.4"/>
      <path d="M6 5 L21 11 M6 9 L21 3" stroke="#111" stroke-width="1.4"/>
    </svg>
    <svg class="edge-arrow edge-arrow--top" viewBox="0 0 10 10" aria-hidden="true"><path d="M0 8 L5 2 L10 8Z" fill="#fff"/></svg>
    <svg class="edge-arrow edge-arrow--bottom" viewBox="0 0 10 10" aria-hidden="true"><path d="M0 2 L5 8 L10 2Z" fill="#fff"/></svg>
    <svg class="edge-arrow edge-arrow--left" viewBox="0 0 10 10" aria-hidden="true"><path d="M8 0 L2 5 L8 10Z" fill="#fff"/></svg>
    <svg class="edge-arrow edge-arrow--right" viewBox="0 0 10 10" aria-hidden="true"><path d="M2 0 L8 5 L2 10Z" fill="#fff"/></svg>

    <div class="card-face">
      <div class="brand-block">
        <span class="brand-rule"></span>
        <div class="brand-name">Velta<br>Motorhof</div>
        <div class="brand-slogan">european automotive specialist</div>
      </div>

      <div class="office office--uk">
        <h3 class="office-name">United Kingdom:</h3>
        <address class="office-address">Lorem ipsum dolor sit amet, consectetur<br>adipiscing elit. Phasellus non.</address>
      </div>
      <div class="office office--sg">
        <h3 class="office-name">Singapore:</h3>
        <address class="office-address">Vestibulum accumsan dignissim tellus,<br>id luctus neque hendrerit nec. Sed.</address>
      </div>
    </div>
  </section>

  <div class="side-label side-label--back">Back</div>

  <section class="print-sheet print-sheet--back" aria-label="Card back">
    <div class="bleed-zone"></div>
    <span class="guide-tag guide-tag--bleed">BLEED</span>
    <span class="guide-tag guide-tag--trim">TRIM</span>
    <svg class="scissors" viewBox="0 0 22 14" aria-hidden="true">
      <circle cx="4" cy="4" r="2.6" fill="none" stroke="#111" stroke-width="1.4"/>
      <circle cx="4" cy="10" r="2.6" fill="none" stroke="#111" stroke-width="1.4"/>
      <path d="M6 5 L21 11 M6 9 L21 3" stroke="#111" stroke-width="1.4"/>
    </svg>
    <svg class="edge-arrow edge-arrow--top" viewBox="0 0 10 10" aria-hidden="true"><path d="M0 8 L5 2 L10 8Z" fill="#fff"/></svg>
    <svg class="edge-arrow edge-arrow--bottom" viewBox="0 0 10 10" aria-hidden="true"><path d="M0 2 L5 8 L10 2Z" fill="#fff"/></svg>
    <svg class="edge-arrow edge-arrow--left" viewBox="0 0 10 10" aria-hidden="true"><path d="M8 0 L2 5 L8 10Z" fill="#fff"/></svg>
    <svg class="edge-arrow edge-arrow--right" viewBox="0 0 10 10" aria-hidden="true"><path d="M2 0 L8 5 L2 10Z" fill="#fff"/></svg>

    <div class="card-face">
      <svg class="corner-swoosh" viewBox="0 0 240 72" preserveAspectRatio="none" aria-hidden="true">
        <defs>
          <linearGradient id="swooshFill" x1="0" y1="0" x2="1" y2="1">
            <stop offset="0" stop-color="#0b9fd8"/>
            <stop offset="1" stop-color="#2cc6f2"/>
          </linearGradient>
        </defs>
        <path d="M0 0 L240 0 L240 72 C200 30 120 6 0 0Z" fill="url(#swooshFill)"/>
        <path d="M0 0 C120 6 200 30 240 72" fill="none" stroke="#9fe6ff" stroke-width="1.5" opacity=".7"/>
      </svg>

      <div class="holder">
        <h1 class="holder-name">Marcus Ellory</h1>
        <div class="holder-rule"></div>
        <span class="holder-title">vice president</span>
      </div>

      <div class="info-block info-block--address">
        <h3 class="info-label">Address :</h3>
        <address class="info-text">Phasellus vitae enim mauris.<br>Suspendisse eget lacinia magna. In<br>dolor urna, scelerisque sit amet dignissim<br>sed, volutpat et nulla. Aliquam</address>
      </div>
      <div class="info-block info-block--contact">
        <h3 class="info-label">Contact:</h3>
        <p class="info-text info-text--contact">Home : (+62) 555014367<br>Phone : (+62) 8955501541</p>
      </div>
    </div>
  </section>
</body>
</html>
```